Web Header Banner

I require a web header banner for a website about the cloud.
The banner should be modern, and look professional. And not contain real clouds.
This will be say 'Confused about The Cloud ?
The background will be blue #3399ff and it should be aim for IT professionals.

Target Market(s)

IT Professionals

Industry/Entity Type

It Professional

Requirements
Must have
• Be modern. Not cartoony
Nice to have
• A women looking confused
• Various line pictures of cloud object above head.
• In a ligter blue then the main background. Much like the background to quillnest.
• https://www.quillnest-example.com/business
• Must contain the wording.... Confused about The Cloud?
Should not have
• real life clouds

```html
<!DOCTYPE html>
<html lang="en">
<head>
<meta charset="utf-8">
<title>Think Cloud – Web Header Banner</title>
<link rel="stylesheet" href="https://fonts.googleapis.com/css2?family=Open+Sans:wght@800&display=swap">
<style>
  :root {
    --sky-deep: #2f8fd6;
    --sky-mid: #5aaee6;
    --sky-light: #a9d6f3;
    --outline-blue: #1a7ab8;
    --bubble-white: #ffffff;
    --hair-brown: #5a3a2a;
    --top-black: #1b1b1f;
    --skin-tone: #d9a48a;
  }
  html, body {
    margin: 0;
    padding: 0;
    overflow: hidden;
    background: #ffffff;
  }
  .banner {
    position: relative;
    width: 1200px;
    height: 750px;
    overflow: hidden;
  }
  .sky-backdrop {
    position: absolute;
    inset: 0;
    background:
      radial-gradient(ellipse 520px 260px at 20% 30%, rgba(255,255,255,0.55), transparent 70%),
      radial-gradient(ellipse 560px 220px at 85% 80%, rgba(255,255,255,0.6), transparent 70%),
      radial-gradient(ellipse 420px 200px at 10% 90%, rgba(255,255,255,0.5), transparent 70%),
      linear-gradient(160deg, var(--sky-light) 0%, var(--sky-mid) 45%, var(--sky-deep) 100%);
  }
  .portrait-area {
    position: absolute;
    left: 315px;
    top: 368px;
    width: 540px;
    height: 382px;
    border-radius: 220px 220px 0 0;
    background:
      radial-gradient(ellipse 90px 120px at 55% 30%, var(--skin-tone), transparent 75%),
      linear-gradient(180deg, var(--hair-brown) 0%, var(--hair-brown) 55%, var(--top-black) 100%);
    opacity: 0.92;
  }
  .headline-art,
  .thought-art {
    position: absolute;
    inset: 0;
  }
  .headline-text {
    font-family: "Open Sans", sans-serif;
    font-weight: 800;
    font-size: 92px;
    fill: var(--bubble-white);
    stroke: var(--outline-blue);
    stroke-width: 20px;
    stroke-linejoin: round;
    paint-order: stroke fill;
  }
  .bubble-puff { fill: var(--bubble-white); }
  .cloud-icon {
    fill: var(--bubble-white);
    stroke: var(--outline-blue);
    stroke-width: 11;
    stroke-linejoin: round;
  }
</style>
</head>
<body>
<main class="banner">
  <div class="sky-backdrop" role="img" aria-label="Soft blue sky background"></div>
  <div class="portrait-area" role="img" aria-label="Photo of a young woman in glasses scratching her head, looking up in confusion"></div>

  <svg class="thought-art" viewBox="0 0 1200 750" width="1200" height="750" aria-hidden="true">
    <defs>
      <path id="cloud-shape" d="M40,120 a40,40 0 0,1 -4,-80 a58,58 0 0,1 104,-22 a44,44 0 0,1 62,42 a30,30 0 0,1 -4,60 z"/>
    </defs>
    <g class="thought-bubble">
      <circle class="bubble-puff" cx="700" cy="125" r="95"/>
      <circle class="bubble-puff" cx="800" cy="70" r="90"/>
      <circle class="bubble-puff" cx="920" cy="70" r="95"/>
      <circle class="bubble-puff" cx="1020" cy="135" r="95"/>
      <circle class="bubble-puff" cx="950" cy="200" r="90"/>
      <circle class="bubble-puff" cx="820" cy="210" r="95"/>
      <circle class="bubble-puff" cx="720" cy="205" r="70"/>
      <circle class="bubble-puff" cx="860" cy="140" r="110"/>
      <circle class="bubble-puff" cx="745" cy="352" r="32"/>
      <circle class="bubble-puff" cx="790" cy="340" r="38"/>
      <circle class="bubble-puff" cx="775" cy="372" r="30"/>
      <circle class="bubble-puff" cx="818" cy="366" r="28"/>
      <circle class="bubble-puff" cx="690" cy="430" r="20"/>
      <circle class="bubble-puff" cx="708" cy="422" r="19"/>
      <circle class="bubble-puff" cx="700" cy="440" r="17"/>
    </g>
    <g class="cloud-icons">
      <use href="#cloud-shape" class="cloud-icon" transform="translate(815,45) scale(0.95)"/>
      <use href="#cloud-shape" class="cloud-icon" transform="translate(760,80) scale(0.95)"/>
      <use href="#cloud-shape" class="cloud-icon" transform="translate(705,120) scale(1.05)"/>
    </g>
  </svg>

  <svg class="headline-art" viewBox="0 0 1200 750" width="1200" height="750">
    <text class="headline-text" x="110" y="335">Think</text>
    <text class="headline-text" x="110" y="470">Cloud</text>
  </svg>
</main>
</body>
</html>
```